Need Business Cards for my Business

email address: rkpmarlowhollowworks@vendrimail.com
web address: rkpmarlowhollowworks.net
Slogan: We offer various QVN licenses
Rowland K. Pemberly
Please stick with colors of Company Logo
would like the card to be more of the color example of the logo.
If you need PDF copy of logo email me at the above account.
Creative control rests with you.

Industry/Entity Type

Business

Contact Information for Business Card

I am a minimalist, but would like something to pop and stand out amongst other cards, make it memorable.

Font styles to use
Serif
Decorative
Script

```html
<!DOCTYPE html>
<html lang="en">
<head>
<meta charset="utf-8">
<title>RKP Marlow Hollow Works — Business Card</title>
<link rel="stylesheet" href="https://fonts.googleapis.com/css2?family=Cormorant+SC:wght@600&family=Questrial&display=swap">
<style>
  :root {
    --backdrop: #1e1e1e;
    --card: #ffffff;
    --ink: #1a1a1a;
    --ink-soft: #3a3a3a;
    --brand: #2b2b2b;
    --rule: #9a9a9a;
    --mark-faint: #e6e6e8;
  }
  * { margin: 0; padding: 0; box-sizing: border-box; }
  html, body {
    width: 1200px; height: 1120px; overflow: hidden;
    background: var(--backdrop);
  }
  .canvas {
    position: relative; width: 1200px; height: 1120px;
    display: flex; align-items: center; justify-content: center;
  }
  .card {
    position: relative; width: 1000px; height: 572px;
    background: var(--card);
    box-shadow: 0 20px 50px rgba(0,0,0,.5);
    font-family: "Questrial", sans-serif;
    color: var(--ink);
  }
  .card__mark-faint {
    position: absolute; left: 40px; top: 40px;
    width: 200px; height: 200px; border-radius: 50%;
    background: var(--mark-faint);
  }
  .divider { position: absolute; width: 1px; background: var(--rule); }
  .divider--top { left: 530px; top: 0; height: 255px; }
  .divider--bottom { left: 500px; top: 305px; height: 240px; }

  .identity { position: absolute; left: 560px; top: 45px; width: 380px; }
  .identity__name {
    font-family: "Cormorant SC", serif; font-weight: 600;
    font-size: 34px; line-height: 1.0; letter-spacing: .5px; color: var(--ink);
  }
  .identity__rule { height: 1px; background: var(--rule); margin: 6px 0 6px; }
  .identity__title { font-size: 19px; color: var(--ink-soft); padding-left: 18px; }

  .brand {
    position: absolute; left: 560px; top: 300px; width: 400px;
    display: flex; align-items: center; gap: 16px;
  }
  .brand__dot { width: 34px; height: 34px; border-radius: 50%; background: var(--brand); flex: none; }
  .brand__name {
    font-size: 34px; line-height: 1.1; color: var(--brand);
    text-transform: uppercase; letter-spacing: 1px;
  }

  .contact {
    position: absolute; right: 525px; top: 330px; width: 440px;
    text-align: right;
  }
  .contact__phone { font-size: 22px; font-weight: 700; line-height: 1.45; color: var(--ink); letter-spacing: .5px; }
  .contact__email { font-size: 17px; margin-top: 4px; color: var(--ink-soft); }
  .contact__address { font-size: 17px; line-height: 1.3; margin-top: 16px; color: var(--ink-soft); }
  .contact__web { font-size: 17px; margin-top: 18px; color: var(--ink-soft); }
</style>
</head>
<body>
<main class="canvas">
  <article class="card">
    <div class="card__mark-faint" aria-hidden="true"></div>
    <span class="divider divider--top"></span>
    <span class="divider divider--bottom"></span>

    <header class="identity">
      <h1 class="identity__name">Rowland<br>K. Pemberly</h1>
      <div class="identity__rule"></div>
      <p class="identity__title">President</p>
    </header>

    <div class="brand">
      <span class="brand__dot" aria-hidden="true"></span>
      <p class="brand__name">RKP Marlow<br>Hollow Works</p>
    </div>

    <address class="contact" style="font-style:normal">
      <p class="contact__phone">410.555.0182</p>
      <p class="contact__phone">610.555.0247</p>
      <p class="contact__email">rkpmarlowhollowworks@vendrimail.com</p>
      <p class="contact__address">2270 Larkmoor Ave, Ste 4<br>Cedar Vale, CA. 90311</p>
      <p class="contact__web">www.rkpmarlowhollowworks.net</p>
    </address>
  </article>
</main>
</body>
</html>
```